Business Card for Pottery and Jewellery Designer

A new business card design is needed to accompany a newly launching pottery and jewellery website. The company logo has been attached for use. The company is called Glazewick Studio. For a sense of the vibe please see the website (it is currently under construction but this way you'll get a feel for the style) www.GlazewickStudio.com

The website font is Pontano Sans for the body of the text with Overlock for headers.

The overall look should be clean and elegant. The back side can have just the logo. The front side should have a smaller logo and the following details displayed:

Glazewick Studio
Designer: Hollis Marrow
Phone: xxx.xxx.xxxx
Email: Designer@GlazewickStudio.com

The structure of displaying this is completely up to you. Different layouts and creative methods of displaying contact info are welcome as long as it stays clean/uncluttered.

No product photographs are to be included in the design as the catalogue changes quickly.

Colour preferences lean towards elegant and understated (charcoal grey, dark navy blue etc.)

Please let me know if you have any further questions or further details required.

Target Market(s)

Target market is 30+ year old women

Industry/Entity Type

Construction

Colors
ffffff
1b1b1b
474747
d9d9d9
fafafa
0355a3

Requirements
Must have
• The submissions so far have looked very typical and don't stand out right now. They're also all in navy with very little variation. I'm looking for something that stands out a it more while still being clean-looking.
Nice to have
• I've attached a few design samples and an idea for a backdrop. It would be great to see some designs in black, white, and grey with only a hint of color.
Should not have
• Product Images

```html
<!DOCTYPE html>
<html lang="en">
<head>
<meta charset="utf-8">
<title>Glazewick Studio – Business Card</title>
<link rel="stylesheet" href="https://fonts.googleapis.com/css2?family=Cinzel:wght@400;500&family=EB+Garamond:wght@400;500&family=Cormorant+Garamond:ital,wght@1,400&display=swap">
<style>
  :root {
    --backdrop: #e6e6e6;
    --card: #fafafa;
    --card-white: #ffffff;
    --ink: #1b1b1b;
    --charcoal: #474747;
    --mid-grey: #8a8a8a;
    --rule-light: #d9d9d9;
    --accent: #0355a3;
    --card-shadow: rgba(0, 0, 0, 0.16);
  }
  * { box-sizing: border-box; margin: 0; padding: 0; }
  html, body {
    width: 1200px;
    height: 900px;
    overflow: hidden;
    background: var(--backdrop);
  }
  .canvas {
    position: relative;
    width: 1200px;
    height: 900px;
  }
  .card {
    position: absolute;
    width: 630px;
    height: 360px;
    background: linear-gradient(160deg, var(--card-white) 0%, var(--card) 60%, #efefef 100%);
    border-radius: 16px;
    box-shadow: 0 10px 28px var(--card-shadow);
    overflow: hidden;
  }
  .card--back { left: 60px; top: 60px; }
  .card--front { left: 510px; top: 480px; }

  /* Back: large brand name */
  .brand-large {
    position: absolute;
    inset: 0;
    display: flex;
    flex-direction: column;
    align-items: center;
    justify-content: center;
    gap: 24px;
  }
  .brand-large .brand-dot {
    width: 84px; height: 84px;
    border-radius: 50%;
    background: var(--charcoal);
  }
  .brand-large .brand-name {
    font-family: "Cinzel", serif;
    font-weight: 400;
    font-size: 44px;
    letter-spacing: 4px;
    color: var(--ink);
  }
  .brand-large .accent-line {
    width: 60px;
    height: 3px;
    background: var(--accent);
    border-radius: 2px;
  }

  /* Front */
  .person {
    position: absolute;
    right: 60px;
    top: 36px;
  }
  .person__name {
    font-family: "Cinzel", serif;
    font-size: 21px;
    letter-spacing: 1px;
    color: var(--ink);
  }
  .person__role {
    font-family: "Cormorant Garamond", serif;
    font-style: italic;
    font-size: 30px;
    color: var(--accent);
    margin-left: 70px;
    margin-top: -2px;
  }
  .brand-small {
    position: absolute;
    left: 44px;
    top: 84px;
    display: flex;
    flex-direction: column;
    align-items: flex-start;
    gap: 10px;
  }
  .brand-small .brand-dot {
    width: 50px; height: 50px;
    border-radius: 50%;
    background: var(--charcoal);
  }
  .brand-small .brand-name {
    font-family: "Cinzel", serif;
    font-size: 20px;
    letter-spacing: 2px;
    color: var(--ink);
    line-height: 1.15;
    width: 150px;
  }
  .contact {
    position: absolute;
    left: 214px;
    top: 168px;
    list-style: none;
    font-family: "EB Garamond", serif;
    font-size: 18px;
    font-weight: 500;
    color: var(--ink);
  }
  .contact li {
    display: flex;
    align-items: center;
    gap: 12px;
    height: 30px;
  }
  .contact svg { width: 18px; height: 16px; fill: var(--charcoal); }
  .contact .contact__web {
    color: var(--mid-grey);
    font-weight: 400;
    padding-left: 30px;
  }
  .rule {
    position: absolute;
    right: 60px;
    height: 2px;
    border-radius: 2px;
  }
  .rule--top {
    left: 214px;
    top: 154px;
    background: linear-gradient(90deg, transparent, var(--rule-light) 25%, var(--rule-light));
  }
  .rule--bottom {
    left: 130px;
    top: 272px;
    height: 3px;
    background: linear-gradient(90deg, var(--rule-light), var(--charcoal) 45%, var(--accent) 60%, var(--rule-light));
  }
  .tagline {
    position: absolute;
    left: 0; right: 0;
    top: 286px;
    text-align: center;
    font-family: "EB Garamond", serif;
    font-size: 14px;
    letter-spacing: 1px;
    line-height: 1.6;
    text-transform: uppercase;
    color: var(--charcoal);
  }
</style>
</head>
<body>
<main class="canvas">

  <section class="card card--back" aria-label="Card back">
    <div class="brand-large">
      <span class="brand-dot"></span>
      <span class="brand-name">Glazewick Studio</span>
      <span class="accent-line"></span>
    </div>
  </section>

  <section class="card card--front" aria-label="Card front">
    <div class="person">
      <p class="person__name">Hollis Marrow</p>
      <p class="person__role">Designer</p>
    </div>

    <div class="brand-small">
      <span class="brand-dot"></span>
      <span class="brand-name">Glazewick Studio</span>
    </div>

    <div class="rule rule--top"></div>

    <ul class="contact">
      <li>
        <svg viewBox="0 0 18 16" aria-hidden="true"><path d="M2 5c0-2 3-4 7-4s7 2 7 4v1h-4V4.5H6V6H2z M4 7h10l2 7H2z"/></svg>
        <span>1300 555 019</span>
      </li>
      <li>
        <svg viewBox="0 0 18 16" aria-hidden="true"><path d="M1 2h16v12H1z M2.5 3.5l6.5 5 6.5-5" stroke="#fafafa" stroke-width="1.2"/></svg>
        <span>Designer@GlazewickStudio.com</span>
      </li>
      <li class="contact__web">www.GlazewickStudio.com</li>
    </ul>

    <div class="rule rule--bottom"></div>

    <p class="tagline">Glazewick Studio offers hand<br>crafted designer jewellery, pottery and artwork.</p>
  </section>

</main>
</body>
</html>
```